I have an existing corporate logo. I'd like to clean it up bit (sharpen it up) and make it look better (without major redesign). I'd like to get the logo itself in all major file formats for print, web, etc.
Then I'd like a business card design that reflects a strategy consulting firm. It should be clean - logo and text without major graphics, and perhaps some small color treatments that match the logo color. The card should suggest high quality in terms of the company.
I'd like the files for card in all major print formats.
Target Market(s)
Silver Birch Partners is a strategy development and business consulting firm focused on small to mid-sized companies. We specialize in business strategy, comprehensive business plan development, market segmentation and positioning, financial models, marketing and sales strategy, product strategy and the effective use of social media in business growth. We operate as consultants, advisers, retained members of management teams, and Board members. We often serve in the role of Chief Strategy Officer, supporting CEO's and other senior executives to enhance top and bottom line growth.
Our overall approach with clients is to deliver actual results, and we often take an active team role with business founders and management teams to drive business growth and affect real changes in performance. As a result, we approach each situation uniquely and partner with clients in a manner that will have the biggest impact on enterprise value.
Industry/Entity Type
Business
Look and feel

```html
<!DOCTYPE html>
<html lang="en">
<head>
<meta charset="utf-8">
<title>Silver Birch Partners – Business Card</title>
<link href="https://fonts.googleapis.com/css2?family=Quicksand:wght@500;600;700&display=swap" rel="stylesheet">
<style>
  :root{
    --navy:#3d3875;
    --paper:#ffffff;
    --backdrop:#d9dbde;
  }
  html,body{margin:0;padding:0;overflow:hidden;}
  body{width:1200px;height:1000px;background:var(--backdrop);position:relative;font-family:"Quicksand",sans-serif;}
  .card{position:absolute;left:100px;top:215px;width:1000px;height:570px;background:var(--paper);overflow:hidden;box-shadow:0 6px 18px rgba(0,0,0,.18);}
  .card-bands{position:absolute;inset:0;}
  .card-bands polygon,.card-bands rect{fill:var(--navy);}

  .brand{position:absolute;left:625px;top:34px;display:flex;align-items:center;gap:14px;color:var(--navy);font-weight:700;}
  .brand-dot{width:30px;height:30px;border-radius:50%;background:var(--navy);flex:none;}
  .brand-name{font-size:26px;line-height:1.1;letter-spacing:.5px;}

  .person{position:absolute;right:560px;top:104px;text-align:right;color:var(--navy);}
  .person-name{margin:0;font-size:36px;font-weight:600;line-height:1;}
  .person-title{margin:4px 0 0;font-size:24px;font-weight:500;line-height:1;}

  .contact{position:absolute;left:345px;margin:0;height:40px;line-height:40px;font-size:22px;font-weight:500;color:var(--navy);white-space:nowrap;}
  .contact.phone{top:200px;}
  .contact.email{top:252px;}
  .contact.web{top:305px;height:41px;line-height:41px;}

  .address{position:absolute;left:80px;top:420px;margin:0;height:70px;line-height:70px;font-size:30px;font-weight:600;letter-spacing:1px;color:var(--navy);white-space:nowrap;}
</style>
</head>
<body>
  <div class="card">
    <svg class="card-bands" width="1000" height="570" viewBox="0 0 1000 570" aria-hidden="true">
      <polygon class="band-top" points="0,0 455,0 415,62 580,62 558,96 0,96"/>
      <rect class="block-left" x="0" y="178" width="330" height="242"/>
      <polygon class="rule-phone" points="330,178 660,178 646,200 330,200"/>
      <polygon class="rule-email" points="330,240 690,240 682,252 330,252"/>
      <polygon class="rule-web" points="330,292 850,292 915,346 705,346 735,304 330,304"/>
      <polygon class="band-lower" points="330,346 960,346 915,420 330,420"/>
      <rect class="band-bottom" x="0" y="490" width="1000" height="80"/>
    </svg>

    <div class="brand">
      <span class="brand-dot"></span>
      <span class="brand-name">Silver Birch<br>Partners, LLC</span>
    </div>

    <div class="person">
      <p class="person-name">Your name</p>
      <p class="person-title">Title</p>
    </div>

    <p class="contact phone">P : 012- 345- 6789</p>
    <p class="contact email">E : yourname@birchmail.com</p>
    <p class="contact web">W : www.birchpartners.com</p>

    <p class="address">The Address Which You Provide</p>
  </div>
</body>
</html>
```